Magazine advertisement

I need a company advertisement for magazine prints. I need to be able to scale it to different sizes if need be. I need it to showcase our brand, VornaDrive have our phone number 582.463.9047 our contact email address sales@vornadrive.net and web address www.vornadrive.net

Target Market(s)

automotive / tractor pulling

Industry/Entity Type

automotive / racing

Colors
EB3D1F
EC4F4E
F09395
F8D3D4
FCEDEE

Requirements
Must have
• our logo, our color scheme (pantone red 1795, white, black, silver

```html
<!DOCTYPE html>
<html lang="en">
<head>
<meta charset="utf-8">
<title>VornaDrive – Magazine Advertisement</title>
<link href="https://fonts.googleapis.com/css2?family=Montserrat:wght@400;500;600&display=swap" rel="stylesheet">
<style>
  :root {
    --page: #e6e6e6;
    --ink: #050505;
    --red: #eb3d1f;
    --red-glow: rgba(150, 28, 16, 0.55);
    --white: #ffffff;
    --silver: #b9bcc0;
    --steel: #5a5d62;
    --muted: #c9c9c9;
  }
  * { margin: 0; padding: 0; box-sizing: border-box; }
  html, body {
    width: 707px; height: 1200px; overflow: hidden;
    background: var(--page);
    font-family: "Montserrat", Arial, sans-serif;
  }
  .advert {
    position: absolute;
    left: 24px; top: 347px;
    width: 660px; height: 505px;
    background: radial-gradient(ellipse 42% 42% at 50% 36%, #1a1a1a 0%, var(--ink) 72%);
    overflow: hidden;
  }
  .advert__product {
    position: absolute;
    left: 200px; top: 60px;
    width: 260px; height: 230px;
    background:
      radial-gradient(circle at 52% 50%, #e4e6e8 0%, var(--silver) 18%, var(--steel) 32%, rgba(20,20,22,0) 46%),
      radial-gradient(ellipse 45% 40% at 30% 55%, var(--red-glow) 0%, rgba(0,0,0,0) 100%);
  }
  .advert__headline {
    position: absolute;
    left: 0; right: 0; top: 394px;
    text-align: center;
    color: var(--white);
    font-size: 11px;
    font-weight: 500;
    letter-spacing: 0.5px;
  }
  .advert__footer {
    position: absolute;
    left: 38px; right: 36px; top: 452px;
    display: flex; align-items: center; justify-content: space-between;
  }
  .contact-list { display: flex; gap: 22px; list-style: none; }
  .contact-list__item {
    display: flex; align-items: center; gap: 6px;
    color: var(--muted); font-size: 8.5px;
  }
  .contact-list__icon { width: 9px; height: 9px; fill: var(--white); }
  .brand {
    display: flex; align-items: center; gap: 6px;
    color: var(--red); font-size: 12px; font-weight: 600;
    letter-spacing: 0.5px; text-transform: uppercase;
  }
  .brand__square { width: 7px; height: 7px; background: var(--red); }
</style>
</head>
<body>
  <section class="advert">
    <div class="advert__product" role="img" aria-label="Photograph of a polished billet turbocharger lit by a soft red glow"></div>
    <h1 class="advert__headline">ENGINEERED TO HAUL &amp; BUILT TO WIN</h1>
    <footer class="advert__footer">
      <ul class="contact-list">
        <li class="contact-list__item">
          <svg class="contact-list__icon" viewBox="0 0 10 10"><path d="M2 0.5 L3.6 0.5 L4.3 2.6 L3.2 3.5 Q4.2 5.8 6.5 6.8 L7.4 5.7 L9.5 6.4 L9.5 8 Q9.5 9.5 8 9.5 Q0.5 9 0.5 2 Q0.5 0.5 2 0.5Z"/></svg>
          582.463.9047
        </li>
        <li class="contact-list__item">
          <svg class="contact-list__icon" viewBox="0 0 10 10"><path d="M0.5 2h9v6h-9z M0.5 2l4.5 3.5 4.5-3.5" fill="none" stroke="#fff" stroke-width="1"/></svg>
          sales@vornadrive.net
        </li>
        <li class="contact-list__item">
          <svg class="contact-list__icon" viewBox="0 0 10 10"><circle cx="5" cy="5" r="4.3" fill="none" stroke="#fff" stroke-width="1"/><path d="M0.7 5h8.6 M5 0.7q-2.5 4.3 0 8.6 M5 0.7q2.5 4.3 0 8.6" fill="none" stroke="#fff" stroke-width="0.8"/></svg>
          www.vornadrive.net
        </li>
      </ul>
      <div class="brand"><span class="brand__square"></span>VornaDrive</div>
    </footer>
  </section>
</body>
</html>
```